Doctors clinic requires stationary designed

We require various types of stationary to be design based on the logo (attached). We require the following:
- Letterhead (A4 Portrait)
- Business Card (must include UV spot on rear)
- With compliments slip (DL Landscape)
- Appointments card (Folded A6)

We are a young clinical practice which boasts a modern and sophisticated approach to medicine so we require something which feels fresh and modern. Please include colours represented in the logo (contrasting teal and grey). We are calling for creative minds to put forth their ideas and we will be actively providing feedback on all designs.

thank you

Clinic

```html
<!DOCTYPE html>
<html lang="en">
<head>
<meta charset="utf-8">
<title>Dr Clara Hollis – Stationery</title>
<link rel="stylesheet" href="https://fonts.googleapis.com/css2?family=Source+Sans+3:wght@300;400;600;700&display=swap">
<style>
:root{
  --board:#3b3b3b;
  --paper:#ffffff;
  --teal:#0a6f6b;
  --teal-text:#137a70;
  --teal-dark:#075d5a;
  --mint:#a9d6c3;
  --rule:#9fc9bd;
  --shadow:0 3px 10px rgba(0,0,0,.45);
}
*{box-sizing:border-box;margin:0;padding:0}
html,body{width:1200px;height:900px;overflow:hidden}
body{background:var(--board);position:relative;font-family:"Source Sans 3",sans-serif;color:var(--teal-text)}
.sheet{position:absolute;background:var(--paper);box-shadow:var(--shadow);overflow:hidden}
.sheet--teal{background:var(--teal);color:#fff}

/* brand lockup */
.brand{position:absolute;display:flex;align-items:center;white-space:nowrap}
.brand__dot{border-radius:50%;border:1.5px solid var(--teal-text);flex:none}
.brand__name{font-weight:600;color:var(--teal-text);letter-spacing:-.2px}
.brand__role{font-weight:600;color:var(--teal-text)}
.brand__divider{width:1px;background:var(--teal-text);align-self:stretch}

.address{position:absolute;font-style:normal;font-size:7px;line-height:1.4;color:var(--teal-text)}
.address strong{font-weight:700}
.address .gap{height:8px}
.sheet--teal .address{color:#fff}

.motif{position:absolute}

/* letterhead */
.letterhead{left:96px;top:105px;width:488px;height:691px}
.letterhead .brand{left:58px;top:40px;gap:6px}
.letterhead .brand__dot{width:40px;height:40px}
.letterhead .brand__name{font-size:15px}
.letterhead .brand__role{font-size:9px;padding-left:4px}
.letterhead .address{left:58px;top:589px}
.letterhead .motif{left:276px;top:460px;width:212px;height:231px;
  background:radial-gradient(circle at 62% 62%,rgba(139,200,175,.55),rgba(169,214,195,.25) 55%,rgba(255,255,255,0) 78%)}

/* business card */
.card-front{left:37px;top:295px;width:207px;height:118px}
.card-front .brand{left:17px;top:15px;gap:4px}
.card-front .brand__dot{width:30px;height:30px}
.card-front .brand__stack{display:flex;flex-direction:column}
.card-front .brand__name{font-size:10.5px;line-height:1}
.card-front .brand__role{font-size:6px}
.card-front .address{left:57px;top:46px;font-size:5px}
.card-front .rule{position:absolute;left:57px;right:0;top:82px;height:1px;background:var(--rule)}
.card-front .web{position:absolute;left:57px;top:85px;font-size:5px;line-height:1.5}
.card-back{left:37px;top:435px;width:207px;height:118px}
.card-back .motif{left:110px;top:10px;width:97px;height:108px;
  background:radial-gradient(circle at 60% 55%,rgba(4,70,67,.75),rgba(4,70,67,.35) 55%,rgba(10,111,107,0) 80%)}

/* appointment card */
.appt-front{left:629px;top:104px;width:243px;height:171px}
.appt-front .brand{left:18px;top:24px;gap:4px}
.appt-front .brand__dot{width:32px;height:32px}
.appt-front .brand__stack{display:flex;flex-direction:column}
.appt-front .brand__name{font-size:11.5px;line-height:1}
.appt-front .brand__role{font-size:6.5px}
.appt-front .rule{position:absolute;left:55px;right:0;top:61px;height:1px;background:var(--rule)}
.appt-front .title{position:absolute;left:58px;top:64px;font-size:14px;font-weight:400;color:var(--teal-dark)}

.appt-back{left:629px;top:320px;width:243px;height:172px}
.appt-back .address{left:22px;top:19px;font-size:6px}
.appt-back .motif{left:130px;top:46px;width:113px;height:126px;
  background:radial-gradient(circle at 60% 55%,rgba(4,70,67,.75),rgba(4,70,67,.35) 55%,rgba(10,111,107,0) 80%)}

.appt-inside{left:920px;top:104px;width:242px;height:344px}
.appt-inside .brand{left:17px;top:12px;gap:4px}
.appt-inside .brand__dot{width:30px;height:30px}
.appt-inside .brand__stack{display:flex;flex-direction:column}
.appt-inside .brand__name{font-size:10.5px;line-height:1}
.appt-inside .brand__role{font-size:6px}
.appt-inside .contact{position:absolute;left:57px;top:45px;font-size:5px;line-height:1.5}
.appt-inside .rule{position:absolute;left:17px;right:16px;height:1px;background:var(--rule)}
.appt-inside .label{position:absolute;left:17px;top:117px;font-size:5px;font-weight:700}
.schedule{position:absolute;left:17px;right:16px;top:126px}
.schedule__row{height:34.3px;position:relative}
.schedule__days{display:flex;justify-content:space-between;font-size:5px;font-weight:700;padding-top:2px}
.schedule__time{position:absolute;left:0;right:0;top:24px;display:flex;align-items:center;gap:3px;font-size:5px;font-weight:700}
.schedule__time span.line{flex:1;height:1px;background:var(--rule)}

/* compliments slip */
.slip{left:629px;top:565px;width:488px;height:230px}
.slip .brand{left:40px;top:27px;gap:6px}
.slip .brand__dot{width:38px;height:38px}
.slip .brand__name{font-size:14px}
.slip .brand__role{font-size:8.5px;padding-left:4px}
.slip .title{position:absolute;left:40px;top:104px;font-size:12.5px;font-weight:400}
.slip .address{left:40px;top:129px;font-size:7px}
.slip .motif{left:300px;top:40px;width:188px;height:190px;
  background:radial-gradient(circle at 55% 55%,rgba(139,200,175,.55),rgba(169,214,195,.25) 55%,rgba(255,255,255,0) 78%)}
</style>
</head>
<body>

<!-- Letterhead -->
<section class="sheet letterhead">
  <div class="brand">
    <span class="brand__dot"></span>
    <span class="brand__name">Dr Clara Hollis</span>
    <span class="brand__divider"></span>
    <span class="brand__role">Obstetrician and Gynaecologist</span>
  </div>
  <address class="address">
    <strong>Northgate Private Hospital</strong><br>
    Suite 14 Spec. Med. Centre (West)<br>
    Harlow Ave, Northgate<br>
    Tel: 9000 1234 Fax: 9000 1235
    <div class="gap"></div>
    <strong>web:</strong>&nbsp; drclarahollis.com.au<br>
    <strong>email:</strong>&nbsp; clara@drclarahollis.com.au
  </address>
  <div class="motif" role="img" aria-label="Large faint mint decorative motif"></div>
</section>

<!-- Business card -->
<section class="sheet card-front">
  <div class="brand">
    <span class="brand__dot"></span>
    <span class="brand__stack">
      <span class="brand__name">Dr Clara Hollis</span>
      <span class="brand__role">Obstetrician and Gynaecologist</span>
    </span>
  </div>
  <address class="address">
    <strong>Northgate Private Hospital</strong><br>
    Suite 14 Spec. Med. Centre (West)<br>
    Harlow Ave, Northgate<br>
    Tel: 9000 1234 Fax: 9000 1235
  </address>
  <div class="rule"></div>
  <div class="web"><strong>web:</strong> drclarahollis.com.au<br><strong>email:</strong> clara@drclarahollis.com.au</div>
</section>
<section class="sheet sheet--teal card-back">
  <div class="motif" role="img" aria-label="UV spot decorative motif in dark teal"></div>
</section>

<!-- Appointment card -->
<section class="sheet appt-front">
  <div class="brand">
    <span class="brand__dot"></span>
    <span class="brand__stack">
      <span class="brand__name">Dr Clara Hollis</span>
      <span class="brand__role">Obstetrician and Gynaecologist</span>
    </span>
  </div>
  <div class="rule"></div>
  <h2 class="title">Appointments card</h2>
</section>

<section class="sheet sheet--teal appt-back">
  <address class="address">
    <strong>Northgate Private Hospital</strong><br>
    Suite 14 Spec. Med. Centre (West)<br>
    Harlow Ave, Northgate<br>
    Tel: 9000 1234 Fax: 9000 1235
    <div class="gap"></div>
    <strong>web:</strong>&nbsp; drclarahollis.com.au<br>
    <strong>email:</strong>&nbsp; clara@drclarahollis.com.au
  </address>
  <div class="motif" role="img" aria-label="Dark teal decorative motif"></div>
</section>

<section class="sheet appt-inside">
  <div class="brand">
    <span class="brand__dot"></span>
    <span class="brand__stack">
      <span class="brand__name">Dr Clara Hollis</span>
      <span class="brand__role">Obstetrician and Gynaecologist</span>
    </span>
  </div>
  <div class="contact">
    <strong>Northgate Private Hospital</strong> Suite 14 Spec. Med. Centre (West)<br>
    Harlow Ave, Northgate Tel: 9000 1234 Fax: 9000 1235<br>
    <strong>web:</strong> drclarahollis.com.au &nbsp;<strong>email:</strong> clara@drclarahollis.com.au
  </div>
  <div class="rule" style="top:75px"></div>
  <div class="rule" style="top:113px"></div>
  <div class="label">Has an appointment on:</div>
  <div class="schedule">
    <div class="schedule__row"><div class="schedule__days"><span>MON</span><span>TUE</span><span>WED</span><span>THU</span><span>FRI</span><span>SAT</span></div><div class="schedule__time"><span class="line"></span>AT<span class="line"></span></div></div>
    <div class="schedule__row"><div class="schedule__days"><span>MON</span><span>TUE</span><span>WED</span><span>THU</span><span>FRI</span><span>SAT</span></div><div class="schedule__time"><span class="line"></span>AT<span class="line"></span></div></div>
    <div class="schedule__row"><div class="schedule__days"><span>MON</span><span>TUE</span><span>WED</span><span>THU</span><span>FRI</span><span>SAT</span></div><div class="schedule__time"><span class="line"></span>AT<span class="line"></span></div></div>
    <div class="schedule__row"><div class="schedule__days"><span>MON</span><span>TUE</span><span>WED</span><span>THU</span><span>FRI</span><span>SAT</span></div><div class="schedule__time"><span class="line"></span>AT<span class="line"></span></div></div>
    <div class="schedule__row"><div class="schedule__days"><span>MON</span><span>TUE</span><span>WED</span><span>THU</span><span>FRI</span><span>SAT</span></div><div class="schedule__time"><span class="line"></span>AT<span class="line"></span></div></div>
    <div class="schedule__row"><div class="schedule__days"><span>MON</span><span>TUE</span><span>WED</span><span>THU</span><span>FRI</span><span>SAT</span></div><div class="schedule__time"><span class="line"></span>AT<span class="line"></span></div></div>
  </div>
</section>

<!-- With compliments slip -->
<section class="sheet slip">
  <div class="brand">
    <span class="brand__dot"></span>
    <span class="brand__name">Dr Clara Hollis</span>
    <span class="brand__divider"></span>
    <span class="brand__role">Obstetrician and Gynaecologist</span>
  </div>
  <h2 class="title">With compliments</h2>
  <address class="address">
    <strong>Northgate Private Hospital</strong><br>
    Suite 14 Spec. Med. Centre (West)<br>
    Harlow Ave, Northgate<br>
    Tel: 9000 1234 Fax: 9000 1235
    <div class="gap"></div>
    <strong>web:</strong>&nbsp; drclarahollis.com.au<br>
    <strong>email:</strong>&nbsp; clara@drclarahollis.com.au
  </address>
  <div class="motif" role="img" aria-label="Large faint mint decorative motif"></div>
</section>

</body>
</html>
```